Business Cards for company that supports physicians that do medical research

Need to create a business card for oKV Lumenta (www.okvlumenta.example), a company devoted to supporting physicians who conduct medical research. The form of the card should match the message of research and information quest. I have provided the logo of the company as an uploaded file. Designs should be simple and slick aimed at very high end clients.

Target Market(s)

Medical doctors that are also researchers

Industry/Entity Type

Medical

Contact Information for Business Card

Should feature logo and fields for personal info:
Name/title
Phone /email

Font styles to use
Serif
Sans Serif

Requirements
Must have
• oKV logo and fields for personal info:
• Name: Bartholomew Okonji
• Title: VP Research and Senior Analyst
• Phone: 418-372-9146
• email: info@okvlumenta.example
Nice to have
• Interesting cards that I've seen:
• 1- all black/charcoal or very dark background
• 2- Plastic - semi-transparent
• 3- non-standard height-width ratios
• 4- Functional cards -- USB drive incorporated
Should not have
• Too busy; needs to stay very simple

```html
<!DOCTYPE html>
<html lang="en">
<head>
<meta charset="utf-8">
<title>oKV Lumenta Business Cards</title>
<link rel="stylesheet" href="https://fonts.googleapis.com/css2?family=Montserrat:wght@600&family=Open+Sans:wght@600&family=Source+Sans+3:wght@400&display=swap">
<style>
  :root {
    --backdrop: #9e9b9b;
    --charcoal: #2b2d31;
    --charcoal-soft: #34373c;
    --paper: #f7f7f7;
    --brand-green: #3aa847;
    --brand-blue: #2f6fb5;
    --accent-blue: #2a90dc;
    --text-light: #e6e7e9;
  }
  * { margin: 0; padding: 0; box-sizing: border-box; }
  html, body {
    width: 1200px; height: 1200px; overflow: hidden;
    background: var(--backdrop);
  }
  .card {
    position: absolute;
    width: 712px; height: 418px;
    border-radius: 22px;
    overflow: hidden;
    background: var(--charcoal);
  }
  .card-front { left: 238px; top: 118px; }
  .card-back { left: 231px; top: 644px; }

  .photo-fill {
    position: absolute; inset: 0;
    background: radial-gradient(ellipse at 75% 40%, var(--charcoal-soft) 0%, var(--charcoal) 65%);
  }

  .wordmark {
    font-family: "Open Sans", sans-serif;
    font-weight: 600;
    color: var(--brand-green);
    white-space: nowrap;
    display: flex; align-items: center; gap: 14px;
  }
  .wordmark .dot {
    width: 16px; height: 16px; border-radius: 50%;
    background: var(--brand-green);
  }
  .card-front .wordmark {
    position: absolute; left: 50%; top: 50%;
    transform: translate(-50%, -50%);
    font-size: 62px; letter-spacing: 1px;
  }

  .back-panel { position: absolute; inset: 0; }
  .card-back .wordmark {
    position: absolute; left: 559px; top: 208px;
    transform: translate(-50%, -50%) rotate(-90deg);
    font-size: 46px; letter-spacing: 1px;
  }

  .holder { position: absolute; left: 45px; top: 38px; }
  .holder-name {
    font-family: "Montserrat", sans-serif; font-weight: 600;
    font-size: 22px; color: var(--accent-blue); letter-spacing: 0.4px;
  }
  .holder-title {
    margin-top: 10px;
    font-family: "Source Sans 3", sans-serif;
    font-size: 17px; color: var(--text-light);
  }

  .contact-list {
    position: absolute; left: 45px; top: 302px;
    list-style: none;
    font-family: "Source Sans 3", sans-serif;
    font-size: 18px; color: var(--text-light);
  }
  .contact-list li {
    display: flex; align-items: center; gap: 11px;
    height: 26.5px;
  }
  .contact-list svg { width: 17px; height: 17px; flex: none; }
</style>
</head>
<body>

<section class="card card-front">
  <div class="photo-fill" role="img" aria-label="Dimmed photo of a stethoscope resting on a keyboard"></div>
  <div class="wordmark"><span class="dot"></span>oKV Lumenta</div>
</section>

<section class="card card-back">
  <div class="photo-fill" role="img" aria-label="Dimmed photo of a stethoscope and pen on a desk"></div>
  <svg class="back-panel" viewBox="0 0 712 418" width="712" height="418" aria-hidden="true">
    <path d="M406 0 C 360 120 368 300 424 418 L712 418 L712 0 Z" fill="var(--paper)"/>
    <path d="M406 0 C 360 120 368 300 424 418" fill="none" stroke="var(--brand-blue)" stroke-width="5"/>
  </svg>

  <div class="holder">
    <div class="holder-name">Bartholomew Okonji</div>
    <div class="holder-title">VP Research &amp; Senior Analyst</div>
  </div>

  <ul class="contact-list">
    <li>
      <svg viewBox="0 0 24 24" aria-hidden="true"><path fill="var(--accent-blue)" d="M3 9c0-3 4-5 9-5s9 2 9 5l-4 1-1-3H8L7 10zM6 12h12l2 8H4z"/><circle cx="12" cy="15.5" r="2" fill="var(--charcoal)"/></svg>
      418-372-9146
    </li>
    <li>
      <svg viewBox="0 0 24 24" aria-hidden="true"><rect x="2" y="5" width="20" height="14" fill="var(--accent-blue)"/><path d="M2 5l10 8 10-8" fill="none" stroke="var(--charcoal)" stroke-width="1.6"/></svg>
      info@okvlumenta.example
    </li>
    <li>
      <svg viewBox="0 0 24 24" aria-hidden="true"><g fill="none" stroke="var(--accent-blue)" stroke-width="1.8"><circle cx="12" cy="12" r="9"/><ellipse cx="12" cy="12" rx="4" ry="9"/><path d="M3 12h18M5 7h14M5 17h14"/></g></svg>
      www.okvlumenta.example
    </li>
  </ul>

  <div class="wordmark"><span class="dot"></span>oKV Lumenta</div>
</section>

</body>
</html>
```